QuillMark Business Cards

I need a business card designed for QuillMark. To get an idea of what we do please visit https://formvault.example/para-creadores-3

```html
<!DOCTYPE html>
<html lang="en">
<head>
<meta charset="utf-8">
<title>QuillMark Business Cards</title>
<link href="https://fonts.googleapis.com/css2?family=Montserrat:wght@700&family=Mulish:wght@400;600&display=swap" rel="stylesheet">
<style>
  :root {
    --backdrop: #e4e4e4;
    --paper: #ffffff;
    --ink: #3a3d44;
    --ink-soft: #5b5e64;
    --gold: #e8a033;
    --slate: #3b3f48;
    --night-1: #3a3e47;
    --night-2: #13161c;
    --name-light: #c9ccd2;
  }
  * { margin: 0; padding: 0; box-sizing: border-box; }
  html, body { width: 1200px; height: 1200px; overflow: hidden; }
  body {
    background: var(--backdrop);
    font-family: "Mulish", sans-serif;
    position: relative;
  }
  .card {
    position: absolute;
    left: 262px;
    width: 686px;
    height: 392px;
    box-shadow: 0 14px 22px rgba(0,0,0,0.18);
  }
  .card--front { top: 165px; background: var(--paper); }
  .card--back {
    top: 653px;
    background: linear-gradient(200deg, var(--night-1) 0%, #22252c 45%, var(--night-2) 100%);
  }

  /* right edge bar */
  .edge-bar { position: absolute; right: 0; width: 7px; background: var(--slate); }
  .edge-bar--top { top: 0; height: 73px; }
  .edge-bar--accent { top: 78px; height: 38px; background: var(--gold); }
  .edge-bar--bottom { top: 121px; bottom: 0; }

  .holder {
    position: absolute;
    right: 59px;
    top: 75px;
    text-align: right;
  }
  .holder__name {
    font-family: "Montserrat", sans-serif;
    font-weight: 700;
    font-size: 24px;
    color: var(--ink);
    letter-spacing: 0.2px;
    line-height: 1.1;
  }
  .holder__title { font-size: 15px; color: var(--gold); line-height: 1.2; }

  .contacts {
    position: absolute;
    right: 59px;
    top: 150px;
    list-style: none;
    font-size: 15.5px;
    color: var(--ink-soft);
  }
  .contacts li {
    display: flex;
    justify-content: flex-end;
    align-items: flex-start;
    line-height: 20.5px;
  }
  .contacts li + li { margin-top: 0; }
  .contacts .gap { margin-top: 5px; }
  .contacts .text { text-align: right; }
  .contacts svg { width: 13px; height: 13px; margin-left: 12px; margin-top: 4px; flex: none; }

  .rule {
    position: absolute;
    height: 1px;
    background: var(--ink);
  }
  .card--front .rule { left: 248px; width: 376px; top: 286px; }

  .website {
    position: absolute;
    right: 59px;
    top: 300px;
    font-size: 16px;
    color: var(--gold);
  }
  .website strong { font-weight: 600; }

  .brand { position: absolute; display: flex; align-items: center; }
  .brand__mark { flex: none; border: 2px solid var(--gold); }
  .brand__name { font-family: "Mulish", sans-serif; font-weight: 400; text-transform: uppercase; }

  .card--front .brand { left: 120px; top: 255px; }
  .card--front .brand__mark { width: 22px; height: 22px; margin-right: 16px; }
  .card--front .brand__name { font-size: 24px; letter-spacing: 6px; color: var(--ink); }

  .card--back .brand { left: 135px; top: 168px; }
  .card--back .brand__mark { width: 40px; height: 40px; margin-right: 32px; }
  .card--back .brand__name { font-size: 38px; letter-spacing: 12px; color: var(--name-light); }
  .card--back .rule { left: 207px; width: 345px; top: 216px; background: #0b0d10; }
</style>
</head>
<body>

<section class="card card--front" aria-label="Business card front">
  <div class="edge-bar edge-bar--top"></div>
  <div class="edge-bar edge-bar--accent"></div>
  <div class="edge-bar edge-bar--bottom"></div>

  <div class="holder">
    <h1 class="holder__name">DANIEL REYES</h1>
    <p class="holder__title">President</p>
  </div>

  <ul class="contacts">
    <li>
      <span class="text">4120 Alder Court<br>Fairbanks, Alaska 99701</span>
      <svg viewBox="0 0 12 12" aria-hidden="true"><path d="M6 0.5a4 4 0 0 0-4 4c0 3 4 7 4 7s4-4 4-7a4 4 0 0 0-4-4z" fill="var(--gold)"/><circle cx="6" cy="4.5" r="1.5" fill="#fff"/></svg>
    </li>
    <li class="gap">
      <span class="text">555-214-7730</span>
      <svg viewBox="0 0 12 12" aria-hidden="true"><path d="M2.5 0.8l2 2.4-1.1 1.4a7 7 0 0 0 4 4l1.4-1.1 2.4 2-1.3 1.7C5.5 11 1 6.5 0.8 2.1z" fill="var(--gold)"/></svg>
    </li>
    <li>
      <span class="text">555-318-6042</span>
      <svg viewBox="0 0 12 12" aria-hidden="true"><rect x="3" y="0.5" width="6" height="11" rx="1" fill="none" stroke="var(--gold)" stroke-width="1.2"/><rect x="5.2" y="9.5" width="1.6" height="0.8" fill="var(--gold)"/></svg>
    </li>
    <li>
      <span class="text">555-407-1195</span>
      <svg viewBox="0 0 12 12" aria-hidden="true"><rect x="3" y="1" width="6" height="4" fill="var(--gold)"/><rect x="0.5" y="5" width="11" height="5" rx="1" fill="var(--gold)"/><rect x="3" y="8" width="6" height="3.5" fill="#fff" stroke="var(--gold)"/></svg>
    </li>
    <li>
      <span class="text">reyes@quillmark.example</span>
      <svg viewBox="0 0 12 12" aria-hidden="true"><rect x="0.5" y="2.5" width="11" height="8" fill="var(--gold)"/><path d="M1 3l5 4 5-4" fill="none" stroke="#fff" stroke-width="1"/></svg>
    </li>
  </ul>

  <div class="brand">
    <span class="brand__mark"></span>
    <span class="brand__name">QuillMark</span>
  </div>
  <div class="rule"></div>

  <p class="website">WWW.<strong>QUILLMARK</strong>.EXAMPLE</p>
</section>

<section class="card card--back" aria-label="Business card back">
  <div class="brand">
    <span class="brand__mark"></span>
    <span class="brand__name">QuillMark</span>
  </div>
  <div class="rule"></div>
</section>

</body>
</html>
```